Brisk Hive 360 Postcard Design, Double-Sided

Please read carefully and see attached. Designers that do not follow these instructions will not be selected. Limit ONE design submission per artist. The ONE design submission shall show both the front and the back designs. Designs must comply with the attached dismensions accounting for the bleed area to prevent designs from being cut off during printing. The attached business card and door tag designs have already been created, printed and are in use. The postcard shall be similar in design to the attached business card and door tag. All of the information that you need is attached. The overall size is 4.12" x 6.12" for the front. The back is different, see attached and scale to match template. I would like the Veteran Owned Business logo added as well. It would also be nice to see my photo incorporated somehow. I like the yellow on the door tag. It helps build contrast and pops out. Again, one design submission per designer that shows both the front and the back.

Target Market(s)

Please read all instructions and see attached.

Industry/Entity Type

Requirements
Must have
• Please read all instructions and see attached.
Nice to have
Should not have

```html
<!DOCTYPE html>
<html lang="en">
<head>
<meta charset="utf-8">
<title>Brisk Hive 360 Postcard – Front and Back</title>
<link rel="stylesheet" href="https://fonts.googleapis.com/css2?family=Poppins:wght@600;700&family=Mulish:wght@400;500&display=swap">
<style>
  :root {
    --page: #e9e9ea;
    --ink: #0b0b0b;
    --panel: #121212;
    --panel-soft: #262626;
    --paper: #ffffff;
    --line: #111111;
    --photo-a: #d9d9d9;
    --photo-b: #8c8f94;
  }
  * { margin: 0; padding: 0; box-sizing: border-box; }
  html, body { width: 1200px; height: 1200px; overflow: hidden; }
  body {
    background: var(--page);
    font-family: "Mulish", "Helvetica Neue", Arial, sans-serif;
    position: relative;
  }
  .card {
    position: absolute;
    left: 207px;
    width: 784px;
    height: 526px;
    background: var(--paper);
    overflow: hidden;
  }
  .card--front { top: 55px; }
  .card--back { top: 617px; }
  .card-shapes { position: absolute; inset: 0; width: 100%; height: 100%; }

  .services-title {
    position: absolute; left: 64px; top: 70px;
    font-family: "Poppins", Arial, sans-serif; font-weight: 700;
    font-size: 28px; color: var(--paper); letter-spacing: 0.2px;
  }
  .services-list {
    position: absolute; left: 64px; top: 104px;
    list-style: none; color: var(--paper);
    font-size: 20px; line-height: 25.6px;
  }
  .services-list li::before { content: "• "; }

  .brand-mark {
    position: absolute; width: 150px; height: 150px;
    background: var(--ink);
    display: flex; align-items: center; justify-content: center; text-align: center;
    font-family: "Mulish", Arial, sans-serif; font-weight: 500;
    color: var(--paper); font-size: 22px; line-height: 1.2;
  }
  .card--front .brand-mark { left: 63px; top: 340px; }
  .card--back .brand-mark { left: 63px; top: 84px; }

  .owner-photo {
    position: absolute; left: 355px; top: 45px; width: 138px; height: 160px;
    background: linear-gradient(180deg, var(--photo-a) 0%, var(--photo-a) 45%, var(--photo-b) 100%);
  }
  .owner-name {
    position: absolute; left: 516px; top: 42px;
    font-family: "Poppins", Arial, sans-serif; font-weight: 600;
    font-size: 25px; color: var(--ink);
  }
  .owner-role {
    position: absolute; left: 516px; top: 78px;
    font-size: 16px; color: var(--ink);
  }
  .promise-list {
    position: absolute; left: 516px; top: 118px;
    list-style: none; font-size: 17px; line-height: 21.5px; color: var(--ink);
  }
  .promise-list li::before { content: "• "; }

  .contact-list {
    position: absolute; list-style: none; font-size: 17px; line-height: 27px;
  }
  .contact-list li { display: flex; align-items: center; gap: 12px; height: 27px; }
  .contact-list svg { width: 14px; height: 14px; flex: none; }
  .card--front .contact-list { left: 472px; top: 384px; color: var(--ink); }
  .card--back .contact-list { left: 62px; top: 381px; color: var(--paper); }

  .stamp-box {
    position: absolute; left: 624px; top: 49px; width: 110px; height: 128px;
    border: 2px solid var(--line);
  }
</style>
</head>
<body>

<section class="card card--front" aria-label="Postcard front">
  <svg class="card-shapes" viewBox="0 0 627 421" preserveAspectRatio="none" aria-hidden="true">
    <defs>
      <linearGradient id="panelTone" x1="0" y1="0" x2="1" y2="1">
        <stop offset="0" stop-color="#2a2a2a"/>
        <stop offset="1" stop-color="#141414"/>
      </linearGradient>
    </defs>
    <polygon points="0,0 277,0 277,181 337,211 337,421 0,421" fill="url(#panelTone)"/>
    <polyline points="304,0 304,181 364,211 364,421" fill="none" stroke="#111" stroke-width="1.6"/>
    <polyline points="337,288 448,288 471,244 627,244" fill="none" stroke="#111" stroke-width="1.6"/>
  </svg>

  <h2 class="services-title">SERVICES:</h2>
  <ul class="services-list">
    <li>Assembly</li>
    <li>Small Repairs</li>
    <li>Wifi / Router Setup</li>
    <li>Fabrication</li>
    <li>Hanging Items</li>
    <li>Wireless Device Setup</li>
    <li>Odd Jobs</li>
  </ul>

  <div class="brand-mark">Brisk Hive<br>360</div>

  <div class="owner-photo" role="img" aria-label="Portrait photo of the owner in a grey polo shirt"></div>
  <h1 class="owner-name">Dale R. Corvan</h1>
  <p class="owner-role">Owner &amp; Handyman</p>
  <ul class="promise-list">
    <li>Fast Response</li>
    <li>High Quality</li>
    <li>Fair Pricing</li>
    <li>Veteran Owned</li>
  </ul>

  <ul class="contact-list">
    <li><svg viewBox="0 0 14 14"><circle cx="7" cy="5" r="3" fill="none" stroke="currentColor" stroke-width="1.6"/><path d="M2 13c1-3 3-4 5-4s4 1 5 4" fill="none" stroke="currentColor" stroke-width="1.6"/></svg>Harbor Point, Florida</li>
    <li><svg viewBox="0 0 14 14"><rect x="1" y="3" width="12" height="8" fill="currentColor"/><path d="M1 3l6 5 6-5" fill="none" stroke="#fff" stroke-width="1"/></svg>service@briskhive360.com</li>
    <li><svg viewBox="0 0 14 14"><path d="M3 1l3 3-2 2c1 2 2 3 4 4l2-2 3 3-2 2C6 12 2 8 1 3z" fill="currentColor"/></svg>(555) 014-3360 Text</li>
    <li><svg viewBox="0 0 14 14"><circle cx="7" cy="7" r="5.5" fill="none" stroke="currentColor" stroke-width="1.4"/><path d="M1.5 7h11M7 1.5c-3 3-3 8 0 11M7 1.5c3 3 3 8 0 11" fill="none" stroke="currentColor" stroke-width="1.2"/></svg>briskhive360.com</li>
  </ul>
</section>

<section class="card card--back" aria-label="Postcard back">
  <svg class="card-shapes" viewBox="0 0 627 421" preserveAspectRatio="none" aria-hidden="true">
    <polygon points="0,0 218,0 218,176 279,216 279,421 0,421" fill="#050505"/>
    <polyline points="244,0 244,176 305,216 305,421" fill="none" stroke="#111" stroke-width="1.6"/>
    <line x1="374" y1="264" x2="587" y2="264" stroke="#111" stroke-width="1.6"/>
    <line x1="374" y1="306" x2="587" y2="306" stroke="#111" stroke-width="1.6"/>
    <line x1="374" y1="347" x2="587" y2="347" stroke="#111" stroke-width="1.6"/>
  </svg>

  <div class="brand-mark">Brisk Hive<br>360</div>

  <ul class="contact-list">
    <li><svg viewBox="0 0 14 14"><circle cx="7" cy="5" r="3" fill="none" stroke="currentColor" stroke-width="1.6"/><path d="M2 13c1-3 3-4 5-4s4 1 5 4" fill="none" stroke="currentColor" stroke-width="1.6"/></svg>Harbor Point, Florida</li>
    <li><svg viewBox="0 0 14 14"><rect x="1" y="3" width="12" height="8" fill="currentColor"/><path d="M1 3l6 5 6-5" fill="none" stroke="#000" stroke-width="1"/></svg>service@briskhive360.com</li>
    <li><svg viewBox="0 0 14 14"><path d="M3 1l3 3-2 2c1 2 2 3 4 4l2-2 3 3-2 2C6 12 2 8 1 3z" fill="currentColor"/></svg>(555) 014-3360 Text</li>
    <li><svg viewBox="0 0 14 14"><circle cx="7" cy="7" r="5.5" fill="none" stroke="currentColor" stroke-width="1.4"/><path d="M1.5 7h11M7 1.5c-3 3-3 8 0 11M7 1.5c3 3 3 8 0 11" fill="none" stroke="currentColor" stroke-width="1.2"/></svg>briskhive360.com</li>
  </ul>

  <div class="stamp-box" aria-label="Stamp area"></div>
</section>

</body>
</html>
```